WE are a specialised tutoring business looking to a have a landing page design

we need a landing page designed for our business. We provide specialised tutoring for children with learning difficulties. I have attached a brief which includes our logo and also the content for the page.

Target Market(s)

parents

Number of Pages Required

1 page

Requirements
Must have
• our existing logo and the content provided

```html
<!DOCTYPE html>
<html lang="en">
<head>
<meta charset="utf-8">
<title>brightroots – specialised learning for children</title>
<link href="https://fonts.googleapis.com/css2?family=Lora:wght@400;700&family=Open+Sans:wght@400;600;700&display=swap" rel="stylesheet">
<style>
  :root {
    --green: #7cc242;
    --green-dark: #6cb232;
    --ink: #333333;
    --body: #555555;
    --muted: #666666;
    --field-border: #b9b9b9;
    --footer-bg: #f7f8fb;
    --white: #ffffff;
  }
  * { box-sizing: border-box; margin: 0; padding: 0; }
  html, body { width: 882px; height: 1200px; overflow: hidden; background: var(--white); }
  body { position: relative; font-family: "Open Sans", Arial, sans-serif; color: var(--ink); }

  .hero { position: absolute; left: 0; top: 0; width: 882px; height: 561px; overflow: hidden;
    background: linear-gradient(90deg, #e9e3dc 0%, #efe9e4 35%, #f3f2f1 60%, #f1f1f1 100%); }
  .hero-photo { position: absolute; left: 0; top: 140px; width: 520px; height: 421px;
    background: radial-gradient(ellipse at 45% 45%, #ead6cb 0%, #e3d5cc 40%, rgba(230,224,218,0) 75%); }
  .hero-desk { position: absolute; left: 0; top: 480px; width: 520px; height: 81px;
    background: linear-gradient(180deg, #cdb9a4 0%, #e8e4e0 100%); opacity: .7; }

  .brand { position: absolute; left: 0; width: 882px; text-align: center; top: 86px; }
  .brand-name { font-family: "Lora", Georgia, serif; font-size: 36px; font-weight: 400; color: var(--green); letter-spacing: -0.5px; line-height: 40px; }
  .brand-tagline { font-family: "Lora", Georgia, serif; font-size: 9.5px; letter-spacing: 1.6px; color: #555; margin-top: 6px; }

  .intro { position: absolute; left: 478px; top: 190px; width: 330px;
    font-family: "Lora", Georgia, serif; font-size: 15.6px; line-height: 25.8px; color: var(--ink); }

  .enquiry { position: absolute; left: 478px; top: 347px; width: 322px; }
  .field { display: flex; align-items: center; height: 35px; background: var(--white); border: 1px solid var(--field-border);
    padding-left: 15px; font-size: 10.5px; color: var(--muted); margin-bottom: 11px; }
  .field svg { margin-right: 8px; }
  .cta { display: block; margin-top: 14px; width: 236px; height: 43px; border-radius: 22px; border: none;
    background: var(--green); color: var(--white); font-family: "Open Sans", Arial, sans-serif; font-weight: 700; font-size: 11.5px; letter-spacing: .3px; }

  .features { position: absolute; top: 620px; left: 81px; width: 740px; display: flex; gap: 35px; }
  .feature { width: 222px; }
  .feature-art { height: 115px; display: flex; align-items: flex-end; }
  .feature-art div { background: linear-gradient(180deg, #e6f3da, #cfe8b8); border-radius: 4px; }
  .feature h2 { font-family: "Lora", Georgia, serif; font-weight: 700; font-size: 16.5px; color: var(--green); margin-top: 18px; line-height: 22px; }
  .feature p { font-size: 11.3px; line-height: 19.6px; color: var(--body); margin-top: 14px; }

  .footer { position: absolute; left: 0; top: 1029px; width: 882px; height: 171px; background: var(--footer-bg); text-align: center; }
  .contact { margin-top: 52px; font-size: 13px; color: #555; display: flex; justify-content: center; align-items: center; gap: 10px; }
  .contact span { display: inline-flex; align-items: center; gap: 7px; }
  .links { margin-top: 18px; font-size: 10.5px; color: #555; word-spacing: 2px; }
  .links .sep { margin: 0 9px; }
  .copy { margin-top: 16px; font-size: 10.5px; color: #555; }
</style>
</head>
<body>
  <section class="hero">
    <div class="hero-photo" role="img" aria-label="Photo of a teacher helping a young boy write at a desk"></div>
    <div class="hero-desk" aria-hidden="true"></div>

    <header class="brand">
      <div class="brand-name">brightroots</div>
      <div class="brand-tagline">specialised learning for children</div>
    </header>

    <p class="intro">brightroots is a team of psychologists and teachers focused on supporting children with social, emotional, and learning difficulties. We provide specialised tutoring and support for children and their families.</p>

    <form class="enquiry">
      <div class="field">
        <svg width="11" height="9" viewBox="0 0 11 9"><rect x="0" y="0" width="11" height="9" rx="1" fill="#666"/><path d="M0.5 1 L5.5 5 L10.5 1" stroke="#fff" stroke-width="1" fill="none"/></svg>
        Email Address
      </div>
      <div class="field">
        <svg width="9" height="10" viewBox="0 0 9 10"><path d="M1.5 0.5 L3.5 0.5 L4 3 L2.8 4 Q4 6.5 5.8 7 L6.8 6 L9 6.8 L9 9 Q8.5 9.8 7 9.6 Q1 8.5 0.2 2 Q0.2 0.8 1.5 0.5 Z" fill="#666"/></svg>
        Phone Number
      </div>
      <button class="cta" type="button">I WOULD LIKE TO KNOW MORE</button>
    </form>
  </section>

  <section class="features">
    <article class="feature">
      <div class="feature-art"><div style="width:98px;height:78px" role="img" aria-label="Line illustration of leafy plants"></div></div>
      <h2>Know the Child</h2>
      <p>We are dedicated to evidence-based assessment and diagnosis. We believe that earlyintervention requires a clear under-standing of the unique challenges faced by the child.This involves assessment and also a dedication to working with children, their parents, and also their preschool and school contexts. This allows us to ensure that any intervention is tailored to the child.</p>
    </article>
    <article class="feature">
      <div class="feature-art"><div style="width:43px;height:87px" role="img" aria-label="Line illustration of a seedling in a pot"></div></div>
      <h2>Meet the Need</h2>
      <p>We provide individualised tutoring for children that focuses on their specific areas of learning need. Our team are dedicated to providing best-practice learning support within an environment of encouragement and care, understanding the impact that learning difficulties can have on broader areas of confidence and self-concept.</p>
    </article>
    <article class="feature">
      <div class="feature-art"><div style="width:41px;height:110px" role="img" aria-label="Line illustration of a taller plant in a pot"></div></div>
      <h2>Watch them Grow</h2>
      <p>We are committed to seeing growth, this requiring strategic intervention and the ability to assess and provide evidence of achievement. Our passion is not only to provide effective support, but also to help children and their families to see this growth, fostering a culture of positivity and engagement in learning.</p>
    </article>
  </section>

  <footer class="footer">
    <div class="contact">
      <span>
        <svg width="13" height="10" viewBox="0 0 13 10"><rect width="13" height="10" rx="1" fill="#7cc242"/><path d="M0.5 1 L6.5 5.5 L12.5 1" stroke="#fff" stroke-width="1.1" fill="none"/></svg>
        hello@brightroots.example
      </span>
      <span style="margin:0 6px">|</span>
      <span>
        <svg width="8" height="12" viewBox="0 0 8 12"><path d="M4 0 A4 4 0 0 1 8 4 C8 7 4 12 4 12 C4 12 0 7 0 4 A4 4 0 0 1 4 0 Z" fill="#7cc242"/><circle cx="4" cy="4" r="1.6" fill="#fff"/></svg>
        12/48 Harbour View Road, Seacliff, 2095
      </span>
    </div>
    <nav class="links">
      Help<span class="sep">|</span>FAQ<span class="sep">|</span>Support<span class="sep">|</span>Sitemap<span class="sep">|</span>Terms Of Use<span class="sep">|</span>Privacy Statement
    </nav>
    <div class="copy">brightroots © 2019 All rights reserved.</div>
  </footer>
</body>
</html>
```